Brightpath Tutors Homepage and Landing Page Redesign

Brightpath Tutors 456 is a premier test preparation, academic consultation, and private tutoring company based in Los Angeles. We offer our tutoring in-person and also online. <br/><br/>We will need three mockups that are as follows:<br/><br/>1. A mockup of a homepage that will be on www.brightpathtutors456.com<br/>2. A mockup of a free-standing true landing page that will be a one-page site where we will direct traffic from a Zindle PPC ad.<br/>3. A mockup of a landing page that will replace a landing page such as the one at www.brightpathtutors456.com/test-prep-services/k-12/sat/ <br/><br/>Please see the word attached for details.

Target Market(s)

Middle School and High School Student Parents, College Students.

Industry/Entity Type

Tutoring

Number of Pages Required

3 page

Colors

Designer to choose colors to be used in the design.

Requirements
Must have
• The design of these 3 pages will need to fit within the overall design of the main website. We're looking for a user-friendly, easy-to-navigate, yet professional design.

```html
<!DOCTYPE html>
<html lang="en">
<head>
<meta charset="utf-8">
<title>Brightpath Tutors – Homepage</title>
<link href="https://fonts.googleapis.com/css2?family=Josefin+Sans:wght@400;600;700&family=Montserrat:wght@400;500;600;700&display=swap" rel="stylesheet">
<style>
:root{
  --teal:#1f8a86;
  --teal-dark:#17716e;
  --orange:#e9603f;
  --red:#e8391d;
  --yellow:#f8eba3;
  --yellow-deep:#f5d73a;
  --ink:#1c1c1c;
  --grey:#555;
  --band:#e9e9e9;
  --dark:#161616;
  --white:#fff;
}
*{box-sizing:border-box;margin:0;padding:0}
html,body{width:1200px;height:4505px;overflow:hidden}
body{font-family:"Montserrat",sans-serif;color:var(--ink);background:var(--white);position:relative}
.abs{position:absolute}
.head{font-family:"Josefin Sans",sans-serif;font-weight:600;letter-spacing:1px;text-transform:uppercase}
.apple{width:30px;height:30px;border-radius:50%;background:var(--yellow-deep);box-shadow:inset -4px -4px 0 #e6bf12}
.center{left:0;width:1200px;text-align:center}

/* header */
.site-header{left:0;top:0;width:1200px;height:102px;background:var(--white)}
.brand{left:222px;top:26px;display:flex;align-items:center;gap:10px;font-family:"Josefin Sans",sans-serif;font-weight:700;font-size:26px;color:var(--teal)}
.brand-dot{width:22px;height:22px;border-radius:50%;background:var(--orange)}
.contact{top:12px;display:flex;align-items:center;gap:8px}
.contact .ic{width:28px;height:28px;border-radius:50%;display:flex;align-items:center;justify-content:center}
.contact small{display:block;font-size:8px;font-weight:600;color:var(--orange);text-transform:uppercase}
.contact b{font-size:12px}
.search{left:952px;top:16px;width:26px;height:26px;border:2px solid var(--orange);border-radius:50%}
.nav{left:440px;top:63px;display:flex;font-size:10px;font-weight:700;text-transform:uppercase}
.nav span{padding:0 15px;border-right:1px solid var(--ink)}
.nav span:last-child{border:none}

/* hero */
.hero{left:0;top:102px;width:1200px;height:640px}
.hero h1{left:222px;top:170px;font-family:"Josefin Sans",sans-serif;font-weight:700;font-size:64px;line-height:66px;color:var(--teal)}
.hero h1 .hot{color:var(--orange)}
.hero p{left:222px;top:380px;font-size:19px;line-height:27px;width:430px}
.btn-teal{left:217px;top:464px;width:256px;height:40px;border-radius:20px;background:var(--teal);color:#fff;font-size:10px;font-weight:700;display:flex;align-items:center;justify-content:space-between;padding:0 14px 0 16px}
.arrow-dot{width:18px;height:18px;border-radius:50%;background:#fff;display:flex;align-items:center;justify-content:center}
.slider-dots{left:39px;top:255px;display:flex;flex-direction:column;gap:9px}
.slider-dots i{width:10px;height:10px;border-radius:50%;border:2px solid var(--teal);display:block}
.slider-dots i:first-child{background:var(--teal)}
.hero-photo{left:760px;top:0;width:440px;height:640px;background:linear-gradient(160deg,#c9b48a 0%,#5f8fb2 50%,#d8453a 100%);opacity:.85}

/* test prep */
.section-title{font-family:"Josefin Sans",sans-serif;font-weight:600;font-size:32px;color:var(--teal);text-transform:uppercase;letter-spacing:1px}
.card{width:366px;height:290px;background:#fff;box-shadow:0 2px 14px rgba(0,0,0,.12);border-top:10px solid var(--orange);text-align:center;padding:30px 32px 0}
.card.teal{background:linear-gradient(135deg,#2b9590,#1d807c);color:#fff;border-top-color:var(--orange)}
.card .icon{width:82px;height:82px;border-radius:50%;background:var(--orange);margin:0 auto 30px;display:flex;align-items:center;justify-content:center}
.card.teal .icon{background:#fff}
.card h3{font-size:15px;font-weight:600;letter-spacing:.5px;margin-bottom:14px}
.card p{font-size:9.5px;line-height:15px}
.pill{display:inline-block;margin-top:14px;padding:6px 14px;border-radius:12px;background:var(--orange);color:#fff;font-size:8.5px;font-weight:700}
.card.teal .pill{background:#fff;color:var(--teal)}

/* stats */
.stats{left:0;top:1595px;width:1200px;height:518px;background:var(--teal)}
.stats h2{top:128px;color:#fff;font-family:"Josefin Sans",sans-serif;font-weight:600;font-size:33px;line-height:38px;letter-spacing:1px}
.stat{width:170px;text-align:center;top:250px}
.stat .ring{width:106px;height:106px;border-radius:50%;background:var(--yellow-deep);border:5px solid var(--orange);margin:0 auto 14px;display:flex;align-items:center;justify-content:center}
.stat .name{font-family:"Josefin Sans",sans-serif;font-weight:600;color:#fff;font-size:33px}
.stat .val{font-family:"Josefin Sans",sans-serif;font-weight:700;color:var(--yellow-deep);font-size:46px;line-height:46px}

/* tutors */
.tutor{top:2309px;width:241px;height:328px;box-shadow:0 2px 14px rgba(0,0,0,.12);background:#fff;text-align:center;color:var(--orange)}
.tutor.feature{background:var(--orange);color:#fff}
.tutor .photo{margin:0 auto;width:204px;height:213px;background:linear-gradient(180deg,#e8e3de,#b9aca0 60%,#2b3444)}
.tutor h4{font-size:16px;font-weight:600;margin-top:20px}
.tutor .spec{font-size:12px;font-weight:500;text-transform:uppercase}
.tutor .school{font-size:7.5px;font-weight:700;margin-top:10px;line-height:10px;text-transform:uppercase}
.btn-outline{height:40px;border:1.5px solid var(--orange);border-radius:20px;color:var(--orange);font-size:9px;font-weight:600;display:flex;align-items:center;gap:14px;padding:0 10px 0 22px;background:#fff}
.btn-outline .arrow-dot{background:var(--orange)}

/* steps */
.steps{left:222px;top:2903px;width:758px;height:184px;background:var(--teal);display:flex;color:#fff}
.step{flex:1;padding:50px 24px 0;text-align:center;border-right:1px dashed rgba(255,255,255,.6)}
.step:last-child{border:none}
.step h5{font-size:11px;font-weight:700;line-height:14px;margin-bottom:10px;text-transform:uppercase}
.step p{font-size:7px;line-height:11px}
.hex{top:2880px;width:54px;height:50px}

/* featured */
.featured{left:0;top:3227px;width:1200px;height:171px;background:var(--band);display:flex;align-items:center;justify-content:space-between;padding:0 76px 0 70px;color:#777}
.featured .lbl{font-size:17px;font-weight:600;letter-spacing:1px}
.featured .pub{font-size:20px;font-weight:700;color:#666}

/* cta */
.cta{left:0;top:3398px;width:1200px;height:774px}
.cta-photo{left:0;top:60px;width:760px;height:714px;background:linear-gradient(180deg,#f4e79b 0%,#d9c58f 55%,#7a8a6a 100%)}
.bubble{left:345px;top:3560px;width:290px;height:240px}
.bubble-text{left:372px;top:3625px;width:236px;text-align:center;color:#fff;font-size:15px;font-weight:600;line-height:18px}
.form-box{left:720px;top:3612px;width:392px;height:495px;background:var(--dark);color:#fff;padding:40px 28px 0;text-align:center}
.form-box h2{font-family:"Josefin Sans",sans-serif;font-weight:700;font-size:30px;line-height:34px;margin:20px 0 30px}
.field{height:30px;background:#3a3a3a;margin-bottom:11px;text-align:left;font-size:9px;padding:10px 10px;color:#ddd}
.send{display:inline-flex;align-items:center;gap:10px;background:var(--red);padding:11px 16px;font-size:12px;font-weight:600;margin-top:24px}

/* footer */
.footer{left:0;top:4172px;width:1200px;height:305px;background:var(--dark);color:#fff}
.footer .brand{color:#fff;top:60px}
.footer .about{left:222px;top:112px;width:220px;font-size:8px;line-height:10px}
.footer .addr{left:222px;top:176px;width:220px;font-size:8px;line-height:10px;display:flex;gap:6px}
.footer .sub{left:222px;top:227px;width:214px;height:26px;border-radius:13px;background:#fff;display:flex;align-items:center;justify-content:space-between;padding-left:14px;font-size:7px;color:#999}
.footer .sub b{width:32px;height:26px;border-radius:0 13px 13px 0;background:var(--red);display:flex;align-items:center;justify-content:center}
.fcol{top:78px}
.fcol h6{font-family:"Josefin Sans",sans-serif;font-weight:400;font-size:20px;margin-bottom:12px}
.fcol li{list-style:none;font-size:8.5px;line-height:23px;text-transform:uppercase}
.fcol li::before{content:"•";color:var(--orange);margin-right:8px}
.fcol.more li{text-transform:none}
.copy{left:0;top:4477px;width:1200px;height:28px;text-align:center;font-size:8px;line-height:28px;color:#333}
</style>
</head>
<body>

<header class="abs site-header">
  <div class="abs brand"><span class="brand-dot"></span>Brightpath Tutors</div>
  <div class="abs contact" style="left:592px">
    <div class="ic" style="background:var(--teal)"><svg width="14" height="14" viewBox="0 0 14 14"><path d="M1 7 13 1 9 13 7 8Z" fill="#fff"/></svg></div>
    <div><small>Mail us now</small><b>contact@brightpathtutors456.com</b></div>
  </div>
  <div class="abs contact" style="left:808px">
    <div class="ic" style="background:var(--orange)"><svg width="14" height="14" viewBox="0 0 14 14"><path d="M3 1 5 4 4 6Q6 9 8 10L10 9 13 11 11 13Q5 13 1 3Z" fill="#fff"/></svg></div>
    <div><small>Call us now</small><b>555 014 2290</b></div>
  </div>
  <div class="abs search"></div>
  <nav class="abs nav"><span>Home</span><span>Academic Support</span><span>Test Prep</span><span>About</span><span>Resources</span><span>Contact</span></nav>
</header>

<section class="abs hero">
  <svg class="abs" style="left:0;top:0" width="1200" height="640" viewBox="0 0 1200 640"><path d="M0 0H1200V560Q1080 660 900 600T560 560 260 610 0 540Z" fill="var(--yellow)"/></svg>
  <div class="abs hero-photo" role="img" aria-label="Photo of two smiling students holding notebooks"></div>
  <div class="abs slider-dots"><i></i><i></i><i></i><i></i></div>
  <div class="abs apple" style="left:222px;top:84px;width:58px;height:58px"></div>
  <h1 class="abs">EXPERIENCED,<br><span class="hot">PROFESSIONAL</span><br>TUTORS</h1>
  <p class="abs">Tutors available for private sessions either in-home in Los Angeles or online, worldwide.</p>
  <div class="abs btn-teal">SCHEDULE YOUR FREE CONSULTATION <span class="arrow-dot"><svg width="8" height="8"><path d="M2 1 6 4 2 7" stroke="var(--teal)" stroke-width="1.6" fill="none"/></svg></span></div>
</section>

<div class="abs apple" style="left:585px;top:805px"></div>
<h2 class="abs center section-title" style="top:846px">Test Prep</h2>

<div class="abs card" style="left:222px;top:918px">
  <div class="icon"><svg width="40" height="34" viewBox="0 0 40 34"><ellipse cx="15" cy="13" rx="12" ry="9" fill="none" stroke="#fff" stroke-width="2.5"/><ellipse cx="26" cy="18" rx="11" ry="8" fill="none" stroke="#fff" stroke-width="2.5"/></svg></div>
  <h3>ACADEMIC TUTORING</h3>
  <p>Work with one of our expert tutors to supplement what you're learning in school. We will help you stay on track or even push you to stay ahead of the game.</p>
  <span class="pill">LEARN MORE</span>
</div>
<div class="abs card teal" style="left:610px;top:918px" role="img" aria-label="Teal panel over a faint photo of a student">
  <div class="icon"><svg width="30" height="36" viewBox="0 0 30 36"><rect x="3" y="5" width="24" height="29" rx="3" fill="none" stroke="var(--teal)" stroke-width="2.5"/><path d="M9 14H21M9 20H21M9 26H17" stroke="var(--teal)" stroke-width="2.5"/></svg></div>
  <h3>K-12 / COLLEGE TEST PREP</h3>
  <p>Work one-on-one with one of our veteran tutors to help you achieve your test prep goals. SAT, ACT, ISEE, SSAT, HSPT, CHSPE, PSAT, and more!</p>
  <span class="pill">LEARN MORE</span>
</div>
<div class="abs card" style="left:222px;top:1233px">
  <div class="icon"><svg width="40" height="30" viewBox="0 0 40 30"><path d="M20 3 37 11 20 19 3 11Z" fill="none" stroke="#fff" stroke-width="2.5"/><path d="M10 15V23Q20 29 30 23V15" fill="none" stroke="#fff" stroke-width="2.5"/></svg></div>
  <h3>GRADUATE TEST PREP</h3>
  <p>Prepare for your graduate-level exam with one of our experienced tutors and customize your learning game plan around your unique needs. GMAT, GRE.</p>
  <span class="pill">LEARN MORE</span>
</div>
<div class="abs card" style="left:610px;top:1233px">
  <div class="icon"><svg width="40" height="32" viewBox="0 0 40 32"><rect x="3" y="8" width="34" height="22" rx="3" fill="none" stroke="#fff" stroke-width="2.5"/><path d="M14 8V3H26V8M3 16H37" stroke="#fff" stroke-width="2.5" fill="none"/></svg></div>
  <h3>PROFESSIONAL TEST PREP</h3>
  <p>Connect with a specialist who can work around your availability and help you pass your unique professional test. CBEST, CSET, TOEFL.</p>
  <span class="pill">LEARN MORE</span>
</div>

<section class="abs stats">
  <div class="abs apple" style="left:585px;top:75px"></div>
  <h2 class="abs center">PROVEN RESULTS FROM A TUTORING<br>COMPANY YOU CAN TRUST</h2>
  <svg class="abs" style="left:220px;top:255px" width="760" height="110" viewBox="0 0 760 110"><path d="M0 0Q40 10 60 50M190 50Q210 110 250 80M380 50Q400 110 450 80M580 50Q600 110 640 80M720 50Q730 100 756 105" fill="none" stroke="#fff" stroke-width="1.5" stroke-dasharray="4 4"/></svg>
  <div class="abs stat" style="left:221px"><div class="ring"><svg width="50" height="40" viewBox="0 0 50 40"><path d="M25 4 48 14 25 24 2 14Z M12 19V30Q25 38 38 30V19" fill="var(--teal)"/></svg></div><div class="name">SAT</div><div class="val">150</div></div>
  <div class="abs stat" style="left:417px"><div class="ring"><svg width="46" height="46" viewBox="0 0 46 46"><rect x="8" y="16" width="32" height="14" rx="7" transform="rotate(-40 24 23)" fill="var(--teal)"/></svg></div><div class="name">ACT</div><div class="val">4</div></div>
  <div class="abs stat" style="left:609px"><div class="ring"><svg width="46" height="44" viewBox="0 0 46 44"><path d="M6 18H40V40H6ZM16 18V10H30V18M23 10V3" fill="var(--teal)" stroke="var(--teal)" stroke-width="2"/></svg></div><div class="name">ISEE</div><div class="val">2.5</div></div>
  <div class="abs stat" style="left:809px"><div class="ring"><svg width="46" height="44" viewBox="0 0 46 44"><circle cx="12" cy="10" r="5" fill="var(--teal)"/><path d="M7 18H17V40H7ZM20 6H42V26H20Z" fill="var(--teal)"/></svg></div><div class="name">CSET</div><div class="val">90%</div></div>
</section>

<div class="abs apple" style="left:580px;top:2178px"></div>
<h2 class="abs center section-title" style="top:2230px">Meet Some of Our Experienced Tutors</h2>

<div class="abs tutor" style="left:222px">
  <div class="photo" role="img" aria-label="Portrait of tutor Owen R."></div>
  <h4>OWEN R.</h4><div class="spec">Specializes in ISEE</div>
  <div class="school">Pacific Institute of Science<br>PhD candidate</div>
</div>
<div class="abs tutor feature" style="left:481px">
  <div class="photo" role="img" aria-label="Portrait of tutor Maya T."></div>
  <h4>MAYA T.</h4><div class="spec">Specializes in SAT</div>
  <div class="school">Eastbrook University<br>B.A. in Politics</div>
</div>
<div class="abs tutor" style="left:740px">
  <div class="photo" role="img" aria-label="Portrait of tutor Leo D."></div>
  <h4>LEO D.</h4><div class="spec">Specializes in HSPT</div>
  <div class="school">Northgate University<br>B.A. in Literature</div>
</div>
<div class="abs btn-outline" style="left:518px;top:2680px">SEE MORE TUTORS <span class="arrow-dot"><svg width="8" height="8"><path d="M2 1 6 4 2 7" stroke="#fff" stroke-width="1.6" fill="none"/></svg></span></div>

<div class="abs apple" style="left:585px;top:2777px"></div>
<h2 class="abs center section-title" style="top:2818px">It's as Easy as 1-2-3</h2>
<div class="abs steps">
  <div class="step"><h5>Answer a few questions<br>about your needs</h5><p>When you enroll, one of our program coordinators will call you to discuss your needs. We'll take notes on what type of tutoring you're looking for, your availability, where you want to meet, and the best test prep plan for your timeline.</p></div>
  <div class="step"><h5>We match you with the<br>perfect tutor</h5><p>One of the most crucial parts of working with a tutor is ensuring that it's a right fit. Once we understand what type of tutor personality will work best for you, we reach out to our tutors to confirm availability and connect you.</p></div>
  <div class="step"><h5>Schedule your first<br>session</h5><p>We can schedule your lessons in person, online, or even in a café or library if you prefer. We're so confident you'll be happy with our services that we offer a satisfaction promise. Ask us for details.</p></div>
</div>
<svg class="abs hex" style="left:305px" viewBox="0 0 54 50"><path d="M14 1H40L53 25 40 49H14L1 25Z" fill="var(--red)" stroke="#fff" stroke-width="3"/><text x="27" y="34" text-anchor="middle" font-family="Josefin Sans,sans-serif" font-weight="700" font-size="26" fill="#fff">1</text></svg>
<svg class="abs hex" style="left:556px" viewBox="0 0 54 50"><path d="M14 1H40L53 25 40 49H14L1 25Z" fill="var(--red)" stroke="#fff" stroke-width="3"/><text x="27" y="34" text-anchor="middle" font-family="Josefin Sans,sans-serif" font-weight="700" font-size="26" fill="#fff">2</text></svg>
<svg class="abs hex" style="left:809px" viewBox="0 0 54 50"><path d="M14 1H40L53 25 40 49H14L1 25Z" fill="var(--red)" stroke="#fff" stroke-width="3"/><text x="27" y="34" text-anchor="middle" font-family="Josefin Sans,sans-serif" font-weight="700" font-size="26" fill="#fff">3</text></svg>
<svg class="abs" style="left:458px;top:2892px" width="26" height="22"><path d="M2 18Q10 6 20 8M14 3 22 8 15 14" stroke="var(--red)" stroke-width="3" fill="none"/></svg>
<svg class="abs" style="left:709px;top:2892px" width="26" height="22"><path d="M2 18Q10 6 20 8M14 3 22 8 15 14" stroke="var(--red)" stroke-width="3" fill="none"/></svg>
<div class="abs btn-outline" style="left:526px;top:3122px">ENROLL TODAY <span class="arrow-dot"><svg width="8" height="8"><path d="M2 1 6 4 2 7" stroke="#fff" stroke-width="1.6" fill="none"/></svg></span></div>

<section class="abs featured">
  <span class="lbl">FEATURED IN</span>
  <span class="pub">Channel Nine</span>
  <span class="pub">Coastline Times</span>
  <span class="pub">Daily Digest</span>
  <span class="pub">Market Weekly</span>
  <span class="pub">Skillfinder</span>
  <span class="pub">Guidebase</span>
</section>

<section class="abs cta">
  <svg class="abs" style="left:0;top:0" width="1200" height="774" viewBox="0 0 1200 774"><path d="M0 30Q150 0 300 40T620 30 930 40 1200 20V774H0Z" fill="var(--yellow)"/></svg>
  <div class="abs cta-photo" role="img" aria-label="Photo of a smiling student reading a book at a desk against a yellow brick wall"></div>
</section>
<svg class="abs bubble" viewBox="0 0 290 240"><ellipse cx="145" cy="105" rx="138" ry="98" fill="#fff"/><ellipse cx="145" cy="105" rx="128" ry="88" fill="var(--red)"/><path d="M90 180 60 235 125 188Z" fill="var(--red)"/></svg>
<div class="abs bubble-text">Our elite teams of tutors has been helping students realize their academic potential for over a decade. Let us do the same for you.</div>
<div class="abs form-box">
  <div class="apple" style="margin:0 auto"></div>
  <h2>SCHEDULE A FREE<br>CONSULTATION TODAY</h2>
  <div class="field">Name:</div>
  <div class="field">E-Mail:</div>
  <div class="field">Phone:</div>
  <div class="field">School Name:</div>
  <div class="field">Home Zip Code:</div>
  <div class="send">SEND EMAIL <svg width="14" height="14" viewBox="0 0 14 14"><path d="M1 7 13 1 9 13 7 8Z" fill="#fff"/></svg></div>
</div>

<footer class="abs footer">
  <div class="abs brand"><span class="brand-dot"></span>Brightpath Tutors</div>
  <p class="abs about">We specialize in SAT, ACT, ISEE, HSPT, CHSPE, GRE, GMAT, CBEST, and CSET prep as well as academic tutoring in Math, Science, English, and Social Studies.</p>
  <div class="abs addr"><svg width="10" height="14" viewBox="0 0 10 14"><path d="M5 14 1 7A4 4 0 1 1 9 7Z" fill="var(--orange)"/></svg><span>1200 Orchard Ave. Suite 300 Westfield,<br>CA 90000 555-014-2290</span></div>
  <div class="abs sub">Your Email Address<b><svg width="12" height="12" viewBox="0 0 14 14"><path d="M1 7 13 1 9 13 7 8Z" fill="#fff"/></svg></b></div>
  <div class="abs fcol" style="left:502px"><h6>Quick Links</h6><ul><li>Home</li><li>Academic Support</li><li>Test Prep</li><li>About</li><li>Resources</li><li>Contact</li></ul></div>
  <div class="abs fcol" style="left:670px"><h6>Populer Services</h6><ul><li>SAT</li><li>ACT</li><li>ISEE</li><li>CHSPE</li><li>GMAT</li><li>CSET</li></ul></div>
  <div class="abs fcol more" style="left:871px"><h6>More Info</h6><ul><li>Tutoring Resources</li><li>FAQ</li><li>Blog</li><li>Tutoring Jobs</li><li>Innovation Scholarship</li><li>Free Diagnostic Test</li></ul></div>
</footer>
<div class="abs copy">© 2007-2020 Brightpath Tutors 456 - All Rights Reserved.</div>

</body>
</html>
```